Card Design to Advertise New Business

I am looking to have a card designed so that I can pass it out to help promote my business. I have never done this before so I honestly do not know where to start with any ideas. I am providing my website address to help. I provide math tutoring, test prep, and schooling options.

I am looking for a card bigger than a business card but smaller than a flyer. Something front and back that I can pass out.

Business Information
Phone: 470-555-0192
Website: www.kelvanostudyhall.example
Address: 418 Brackenfield Rd Ste 340 Marietta GA 30072
Email: kelvanoservices@kelvanomail.example

Services:
Math Tutoring
NEQ & BOW Test Prep
Group and Private Sessions
Fully Accredited Private School

Target Market(s)

Middle and High School Students

Industry/Entity Type

Education

Requirements
Must have
• Information from my website

```html
<!DOCTYPE html>
<html lang="en">
<head>
<meta charset="utf-8">
<title>Kelvano Study Hall – Promo Card</title>
<link rel="stylesheet" href="https://fonts.googleapis.com/css2?family=Noto+Serif:wght@700&display=swap">
<style>
  :root {
    --page: #faf3ee;
    --card: #ffffff;
    --green: #00cc05;
    --ink: #111111;
    --star: #e0301e;
  }
  html, body {
    margin: 0;
    padding: 0;
    width: 1200px;
    height: 800px;
    overflow: hidden;
    background: var(--page);
  }
  .canvas {
    position: relative;
    width: 1200px;
    height: 800px;
  }
  .card {
    position: absolute;
    top: 200px;
    width: 269px;
    height: 403px;
    background: var(--card);
    overflow: hidden;
  }
  .card--front { left: 300px; }
  .card--back  { left: 637px; }
  .card svg { display: block; width: 100%; height: 100%; }
  .shape { fill: var(--green); }
  .text {
    font-family: "Noto Serif", Georgia, serif;
    font-weight: 700;
    fill: var(--ink);
  }
  .brand-name { font-size: 29px; }
  .brand-name--small { font-size: 13.5px; }
  .contact { font-size: 14px; text-anchor: middle; }
  .service { font-size: 20px; text-anchor: middle; }
  .divider-star { font-size: 14px; text-anchor: middle; fill: var(--star); }
  .website { font-size: 14px; text-anchor: middle; }
</style>
</head>
<body>
<main class="canvas">

  <section class="card card--front" aria-label="Card front">
    <svg viewBox="0 0 524 786" xmlns="http://www.w3.org/2000/svg">
      <circle class="shape" cx="261" cy="-116" r="215"/>
      <circle class="shape" cx="182" cy="156" r="25"/>
      <circle class="shape" cx="324" cy="568" r="14"/>
      <circle class="shape" cx="261" cy="881" r="215"/>
      <g class="brand">
        <circle class="shape" cx="96" cy="357" r="34"/>
        <text class="text brand-name" x="144" y="367">Kelvano Study Hall</text>
      </g>
    </svg>
  </section>

  <section class="card card--back" aria-label="Card back">
    <svg viewBox="0 0 524 786" xmlns="http://www.w3.org/2000/svg">
      <circle class="shape" cx="554" cy="-77" r="215"/>
      <circle class="shape" cx="312" cy="63" r="18"/>
      <circle class="shape" cx="261" cy="881" r="215"/>

      <g class="brand brand--small">
        <circle class="shape" cx="100" cy="82" r="28"/>
        <text class="text brand-name--small" x="44" y="134">Kelvano Study Hall</text>
      </g>

      <g class="contact-block">
        <text class="text contact" x="262" y="227">Phone: 470-555-0192</text>
        <text class="text contact" x="262" y="246">Address: 418 Brackenfield Rd Ste 340 Marietta GA 30072</text>
        <text class="text contact" x="262" y="266">Email: kelvanoservices@kelvanomail.example</text>
      </g>

      <g class="services">
        <text class="text service" x="262" y="361">Math Tutoring</text>
        <text class="divider-star" x="262" y="377">★</text>
        <text class="text service" x="262" y="400">NEQ &amp; BOW Test Prep</text>
        <text class="divider-star" x="262" y="419">★</text>
        <text class="text service" x="262" y="440">Group and Private Sessions</text>
        <text class="divider-star" x="262" y="458">★</text>
        <text class="text service" x="262" y="479">Fully Accredited Private School</text>
      </g>

      <text class="text website" x="262" y="608">www.kelvanostudyhall.example</text>
    </svg>
  </section>

</main>
</body>
</html>
```